Travel video blogger needs website design

I need a website designed for my new travel video blog "Roaming Sparrow". I have only just started but need a website that is fairly simple and not too busy. I have a logo which I want on it (I have attached it to this project). I also want a link to all my other social medias on the main page (vidtrekhub, Snapwell and Palnook) and my videos as well. Here is a link to my vidtrekhub page for you to look at: https://www.vidtrekhub.net/channel/QRm4tZ8pWnE2HX57YKccd31v
As I have only just started and I am still trying to find my specific niche, again I need it to be sleek and simple that I can go in and change slightly here and there. I would like these pages on the website: About Me, Videos, Social Media, Blog, Gallery, contact me. for an example I like the look of www.theroamingkinfolk.net website.

I already have the domain and I am with Harborweb with pagecraftr.org. I just want to spend my time getting better and learning about videos then trying to create a website (I am a bit of a perfectionist when I try to do something).

Target Market(s)

Young Adults (majority females) between the ages of 18 and 30 with an interest in travelling.

Industry/Entity Type

Travel Industry

Number of Pages Required

1 page

Colors

Designer to choose colors to be used in the design.

Requirements
Must have
• A like to my Snapwell, Palnook and vidtrekhub channels on the home page
• Must be a nice, simple design
• Must have my logo on the front and name "Roaming Sparrow"
Nice to have
• A nice light, bright coloured theme
Should not have
• A dark coloured theme

```html
<!DOCTYPE html>
<html lang="en">
<head>
<meta charset="utf-8">
<title>Roaming Sparrow — Travel Video Blog</title>
<link rel="stylesheet" href="https://fonts.googleapis.com/css2?family=Poppins:wght@300;400;500&family=Mr+Dafoe&display=swap">
<style>
  :root{
    --ink:#1d1d1f;
    --muted:#555;
    --soft:#777;
    --line:#e6e6e6;
    --page:#ffffff;
    --band:#f7f7f7;
  }
  *{box-sizing:border-box;margin:0;padding:0}
  html,body{width:929px;height:1200px;overflow:hidden;background:var(--page)}
  body{font-family:"Poppins",sans-serif;color:var(--ink);position:relative}

  .site-header{position:relative;height:160px}
  .menu-toggle{position:absolute;left:189px;top:44px}
  .search-toggle{position:absolute;left:731px;top:43px}
  .brand{position:absolute;left:0;right:0;top:24px;text-align:center}
  .brand-mark{display:block;width:58px;height:58px;margin:0 auto 8px;border:1.6px solid var(--ink);border-radius:50%}
  .brand-name{font-size:13px;font-weight:500;letter-spacing:1.2px;text-transform:uppercase}

  .main-nav{position:absolute;top:170px;left:0;right:0;display:flex;justify-content:center;gap:38px}
  .main-nav a{font-size:8.6px;letter-spacing:1.3px;color:var(--muted);text-decoration:none;text-transform:uppercase}

  .destinations{position:absolute;top:223px;left:19px;display:grid;grid-template-columns:repeat(4,218px);grid-auto-rows:218px;gap:6px}
  .tile{position:relative;display:flex;align-items:center;justify-content:center;overflow:hidden}
  .tile-photo{position:absolute;inset:0}
  .tile-name{position:relative;font-family:"Mr Dafoe",cursive;font-size:40px;color:#fff;text-shadow:0 1px 6px rgba(0,0,0,.25)}

  .p1{background:linear-gradient(135deg,#e9dccb,#d8bfa0 55%,#8a92a8)}
  .p2{background:linear-gradient(180deg,#e8e8e6 0%,#27304a 35%,#8a2a2a 75%,#5a4a3a)}
  .p3{background:linear-gradient(120deg,#d9c2a6,#b99d82 50%,#c8ad90)}
  .p4{background:linear-gradient(180deg,#b9a28a,#e0a24e 45%,#3b3024 70%,#1a1714)}
  .p5{background:linear-gradient(180deg,#e8d7a3,#6c7d4f 40%,#3a4a2c 80%,#2e2a24)}
  .p6{background:linear-gradient(140deg,#30517a,#2a5a8c 50%,#1f3c60)}
  .p7{background:linear-gradient(180deg,#6f98bf,#b9c8cf 40%,#8a6a48 70%,#5e4330)}
  .p8{background:linear-gradient(180deg,#1f2c3a,#3c5a82 50%,#e6e2d8 80%)}
  .p9{background:linear-gradient(180deg,#6a8a5a,#5f8a3a 40%,#4e7a2a)}
  .p10{background:linear-gradient(180deg,#d8d8d6,#8c8e8c 55%,#3a3a3a)}
  .p11{background:linear-gradient(180deg,#8ea08a,#4e6a4a 45%,#3f8a8a 75%,#c9604a)}
  .p12{background:linear-gradient(150deg,#2c5a2c,#3f7a3a 50%,#244a24)}

  .site-footer{position:absolute;top:940px;left:0;width:929px;height:260px;background:var(--band);text-align:center}
  .newsletter-title{position:absolute;top:45px;left:0;right:0;font-size:18px;font-weight:400}
  .newsletter-form{position:absolute;top:80px;left:295px;width:339px;height:30px;display:flex;background:#fff;border:1px solid #ececec}
  .newsletter-input{flex:1;border:0;border-right:1px solid #ececec;font:300 7.5px "Poppins",sans-serif;padding-left:10px;color:var(--soft);display:flex;align-items:center}
  .newsletter-button{width:97px;display:flex;align-items:center;justify-content:center;font-size:7.5px;color:var(--ink)}
  .footer-nav{position:absolute;top:138px;left:0;right:0;display:flex;justify-content:center;gap:28px}
  .footer-nav a{font-size:6px;letter-spacing:1px;color:var(--muted);text-decoration:none;text-transform:uppercase}
  .social{position:absolute;top:176px;left:0;right:0;display:flex;justify-content:center;gap:7px}
  .social a{width:18px;height:18px;border:1px solid #bbb;border-radius:50%;display:block}
  .copyright{position:absolute;top:203px;left:0;right:0;font-size:7.5px;font-weight:300;color:var(--muted)}
</style>
</head>
<body>
  <header class="site-header">
    <svg class="menu-toggle" width="16" height="10" viewBox="0 0 16 10" aria-label="Menu">
      <path d="M0 1h15M0 5h12M0 9h9" stroke="#555" stroke-width="1"/>
    </svg>
    <div class="brand">
      <span class="brand-mark" aria-hidden="true"></span>
      <span class="brand-name">Roaming Sparrow</span>
    </div>
    <svg class="search-toggle" width="10" height="10" viewBox="0 0 10 10" aria-label="Search">
      <circle cx="4" cy="4" r="3.2" fill="none" stroke="#555" stroke-width="1"/>
      <path d="M6.4 6.4L9 9" stroke="#555" stroke-width="1"/>
    </svg>
    <nav class="main-nav">
      <a href="#">About Me</a><a href="#">Videos</a><a href="#">Social Media</a><a href="#">Blog</a><a href="#">Gallery</a><a href="#">Contact</a>
    </nav>
  </header>

  <main class="destinations">
    <a class="tile"><span class="tile-photo p1" role="img" aria-label="Selfie of a traveller on a sandy beach"></span><span class="tile-name">Caribbean</span></a>
    <a class="tile"><span class="tile-photo p2" role="img" aria-label="Two children in raincoats at a tent entrance"></span><span class="tile-name">Atlantis</span></a>
    <a class="tile"><span class="tile-photo p3" role="img" aria-label="Bare foot and shadow on sand"></span><span class="tile-name">Nevis</span></a>
    <a class="tile"><span class="tile-photo p4" role="img" aria-label="Golden sunset over a rocky shoreline"></span><span class="tile-name">Indonesia</span></a>
    <a class="tile"><span class="tile-photo p5" role="img" aria-label="Hiker with backpack on a wooden railing above mountains"></span><span class="tile-name">New Zealand</span></a>
    <a class="tile"><span class="tile-photo p6" role="img" aria-label="Folded map tucked in a blue backpack"></span><span class="tile-name">Australia</span></a>
    <a class="tile"><span class="tile-photo p7" role="img" aria-label="Dirt road leading toward rocky hills"></span><span class="tile-name">Cuba</span></a>
    <a class="tile"><span class="tile-photo p8" role="img" aria-label="Traveller writing in a journal with boots up"></span><span class="tile-name">Belize</span></a>
    <a class="tile"><span class="tile-photo p9" role="img" aria-label="Traveller in a sun hat in a green meadow"></span><span class="tile-name">Guatemala</span></a>
    <a class="tile"><span class="tile-photo p10" role="img" aria-label="Outstretched hand over a misty lake"></span><span class="tile-name">Australia</span></a>
    <a class="tile"><span class="tile-photo p11" role="img" aria-label="Traveller sitting on a boat bow near cliffs"></span><span class="tile-name">Cuba</span></a>
    <a class="tile"><span class="tile-photo p12" role="img" aria-label="Aerial view of a road winding through forest"></span><span class="tile-name">Belize</span></a>
  </main>

  <footer class="site-footer">
    <h2 class="newsletter-title">Join the Newsletter</h2>
    <div class="newsletter-form">
      <span class="newsletter-input">Enter your email address</span>
      <span class="newsletter-button">Subscribe</span>
    </div>
    <nav class="footer-nav">
      <a href="#">About Me</a><a href="#">Videos</a><a href="#">Social Media</a><a href="#">Blog</a><a href="#">Gallery</a><a href="#">Contact</a>
    </nav>
    <div class="social">
      <a href="#" aria-label="Palnook" title="Palnook"></a>
      <a href="#" aria-label="Chirply" title="Chirply"></a>
      <a href="#" aria-label="Searchwide" title="Searchwide"></a>
      <a href="#" aria-label="Pinvault" title="Pinvault"></a>
      <a href="#" aria-label="Linkwork" title="Linkwork"></a>
    </div>
    <p class="copyright">© 2018 Roaming Sparrow. All Rights Reserved</p>
  </footer>
</body>
</html>
```